Presentation Folder Art

We need to update our existing presentation folder and need to integrate the various aspects of the testing we do. This isn't easy as our testing is diverse, as seen by the various icon categories we have. We will keep the icons on the inside cover so we don't have an opinion either way if they are kept on the cover or not. A copy of our current folder art is attached (Cover-Diecut-Outlines). I have also uploaded one of our current brochures to see the type of style we're happy with.

Target Market(s)

product manufacturers, importers ranging from commercial to military

Requirements
Must have
• Should integrate our corporate colors of orange and dark blue

```html
<!DOCTYPE html>
<html lang="en">
<head>
<meta charset="utf-8">
<title>Presentation Folder – Global Testing and Approvals</title>
<link rel="stylesheet" href="https://fonts.googleapis.com/css2?family=Montserrat:wght@400;600;700&display=swap">
<style>
  :root {
    --stage: #d9d9db;
    --navy: #0d3f86;
    --blue: #1766b5;
    --blue-light: #3a86d0;
    --orange: #f39a1e;
    --white: #ffffff;
    --inside-left: #8e8f91;
    --inside-right: #9a9b9d;
  }
  html, body {
    margin: 0;
    width: 1200px;
    height: 675px;
    overflow: hidden;
    background: var(--stage);
    font-family: "Montserrat", Arial, sans-serif;
  }
  .canvas {
    position: relative;
    width: 1200px;
    height: 675px;
  }
  .folder-cover {
    position: absolute;
    left: 104px;
    top: 128px;
    width: 290px;
    height: 420px;
  }
  .folder-inside {
    position: absolute;
    left: 455px;
    top: 132px;
    width: 630px;
    height: 422px;
  }
  svg text { font-family: "Montserrat", Arial, sans-serif; }
  .brand-name { font-weight: 700; font-size: 17px; fill: var(--navy); letter-spacing: 0.5px; }
  .headline-accent { font-weight: 700; font-size: 10.5px; fill: var(--orange); }
  .headline { font-weight: 700; font-size: 10.5px; fill: var(--white); }
  .service-label { font-weight: 600; font-size: 4.8px; fill: var(--white); letter-spacing: 0.2px; }
  .icon-label { font-weight: 600; font-size: 3.3px; fill: var(--white); letter-spacing: 0.1px; }
  .icon-glyph { fill: none; stroke: var(--white); stroke-width: 1.3; stroke-linecap: round; stroke-linejoin: round; }
</style>
</head>
<body>
<main class="canvas">

  <!-- Front cover -->
  <svg class="folder-cover" viewBox="0 0 290 420" xmlns="http://www.w3.org/2000/svg">
    <defs>
      <linearGradient id="coverGradient" x1="0" y1="0" x2="0" y2="1">
        <stop offset="0" stop-color="#1766b5"/>
        <stop offset="1" stop-color="#0d3f86"/>
      </linearGradient>
      <linearGradient id="skyTone" x1="0" y1="0" x2="0" y2="1">
        <stop offset="0" stop-color="#b7c4d3"/>
        <stop offset="1" stop-color="#e4e8ec"/>
      </linearGradient>
      <linearGradient id="seaTone" x1="0" y1="0" x2="0" y2="1">
        <stop offset="0" stop-color="#7fb0c8"/>
        <stop offset="1" stop-color="#2f6f92"/>
      </linearGradient>
      <linearGradient id="groundTone" x1="0" y1="0" x2="0" y2="1">
        <stop offset="0" stop-color="#d4d7db"/>
        <stop offset="1" stop-color="#5e636a"/>
      </linearGradient>
    </defs>

    <rect class="cover-background" width="290" height="420" fill="url(#coverGradient)"/>
    <polygon class="cover-band" points="0,300 290,250 290,275 0,330" fill="var(--blue-light)" opacity="0.25"/>

    <polygon class="photo-aircraft" role="img" aria-label="Photo of a military jet flying above clouds"
      points="-40,88 8,0 148,0 194,88 148,174 8,174" fill="url(#skyTone)" stroke="var(--blue-light)" stroke-width="3"/>
    <polygon class="photo-submarine" role="img" aria-label="Photo of a submarine cruising at sea"
      points="150,184 198,96 290,96 290,272 198,272" fill="url(#seaTone)" stroke="var(--blue-light)" stroke-width="3"/>
    <polygon class="photo-vehicle" role="img" aria-label="Photo of an armoured off-road vehicle"
      points="-40,268 8,180 148,180 194,268 148,352 8,352" fill="url(#groundTone)" stroke="var(--blue-light)" stroke-width="3"/>

    <polygon class="brand-panel" points="152,0 290,0 290,64 186,64" fill="var(--white)"/>
    <rect class="brand-mark" x="172" y="22" width="11" height="11" fill="var(--navy)"/>
    <text class="brand-name" x="188" y="33">NORVALE</text>

    <text class="headline-accent" x="250" y="313" text-anchor="end">GLOBAL TESTING</text>
    <text class="headline" x="250" y="326" text-anchor="end">AND APPROVALS</text>
    <circle cx="286" cy="322" r="5" fill="var(--orange)"/>

    <g class="service-list">
      <rect x="16" y="366" width="3" height="3" fill="var(--orange)"/>
      <text class="service-label" x="22" y="369">EMC &amp; TELECOMS</text>
      <rect x="80" y="366" width="3" height="3" fill="var(--orange)"/>
      <text class="service-label" x="86" y="369">SAFETY</text>
      <rect x="118" y="366" width="3" height="3" fill="var(--orange)"/>
      <text class="service-label" x="124" y="369">ENERGY EFFICIENCY</text>
      <rect x="196" y="366" width="3" height="3" fill="var(--orange)"/>
      <text class="service-label" x="202" y="369">ENVIRONMENTAL</text>
    </g>
  </svg>

  <!-- Inside spread with pocket -->
  <svg class="folder-inside" viewBox="0 0 630 422" xmlns="http://www.w3.org/2000/svg">
    <rect class="inside-left-panel" x="0" y="0" width="315" height="422" fill="var(--inside-left)"/>
    <rect class="inside-right-panel" x="315" y="0" width="315" height="422" fill="var(--inside-right)"/>
    <line x1="315" y1="0" x2="315" y2="422" stroke="#7d7e80" stroke-width="1"/>

    <polygon class="pocket" points="305,250 630,250 630,422 292,422" fill="var(--blue)"/>

    <g class="service-icons" transform="translate(0,318)">
      <g transform="translate(340,0)">
        <circle r="10" fill="var(--orange)" stroke="var(--white)" stroke-width="1.2"/>
        <rect class="icon-glyph" x="-4" y="-5" width="8" height="10" rx="1"/>
        <text class="icon-label" y="18" text-anchor="middle">SAFETY</text>
      </g>
      <g transform="translate(377,0)">
        <circle r="10" fill="var(--orange)" stroke="var(--white)" stroke-width="1.2"/>
        <path class="icon-glyph" d="M0 5 V-2 M-4 -4 A6 6 0 0 1 4 -4 M-2 -2 A3 3 0 0 1 2 -2"/>
        <text class="icon-label" y="18" text-anchor="middle">EMC/WIRELESS</text>
      </g>
      <g transform="translate(414,0)">
        <circle r="10" fill="var(--orange)" stroke="var(--white)" stroke-width="1.2"/>
        <path class="icon-glyph" d="M-4 -4 Q-5 3 3 5 L5 3 L2 0 L0 2 Q-2 1 -2 -2 L0 -3 L-2 -6 Z"/>
        <text class="icon-label" y="18" text-anchor="middle">TELECOMMS</text>
      </g>
      <g transform="translate(451,0)">
        <circle r="10" fill="var(--orange)" stroke="var(--white)" stroke-width="1.2"/>
        <path class="icon-glyph" d="M-5 3 A6 6 0 0 1 5 3 M0 3 L3 -2"/>
        <text class="icon-label" y="18" text-anchor="middle">MEPS</text>
      </g>
      <g transform="translate(488,0)">
        <circle r="10" fill="var(--orange)" stroke="var(--white)" stroke-width="1.2"/>
        <path class="icon-glyph" d="M-4 4 Q-4 -4 5 -5 Q4 4 -4 4 M-4 4 L1 -1"/>
        <text class="icon-label" y="18" text-anchor="middle">ENVIRONMENTAL</text>
      </g>
      <g transform="translate(525,0)">
        <circle r="10" fill="var(--orange)" stroke="var(--white)" stroke-width="1.2"/>
        <path class="icon-glyph" d="M-4 0 L-1 3 L5 -4"/>
        <text class="icon-label" y="18" text-anchor="middle">APPROVALS</text>
      </g>
      <g transform="translate(562,0)">
        <circle r="10" fill="var(--orange)" stroke="var(--white)" stroke-width="1.2"/>
        <path class="icon-glyph" d="M-3 3 V-1 A3 3 0 0 1 3 -1 V3 Z M-5 3 H5 M-6 -4 L-5 -3 M6 -4 L5 -3"/>
        <text class="icon-label" y="18" text-anchor="middle">ALARMS</text>
      </g>
      <g transform="translate(599,0)">
        <circle r="10" fill="var(--orange)" stroke="var(--white)" stroke-width="1.2"/>
        <circle class="icon-glyph" cx="0" cy="1" r="4"/>
        <circle class="icon-glyph" cx="-3.5" cy="-3.5" r="1.6"/>
        <circle class="icon-glyph" cx="3.5" cy="-3.5" r="1.6"/>
        <text class="icon-label" y="18" text-anchor="middle">TOYS</text>
      </g>
    </g>
  </svg>

</main>
</body>
</html>
```